wine label for ultra premium vineyard in Ravensdale, High Country, New Zealand

"WREN" is our new wine brand, with grapes grown in our spectacular "ter Bosch" vineyard. The small, elevated vineyard overlooks a river valley and snowy mountains. We would like a highly elegant label for our 2018 pinot noir wine, which highlights the quality of wine and our very special vineyard location. "WREN" has to be prominent, with secondary emphasis on "ter Bosch vineyard" and "Ravensdale, High Country". A stylized WREN logo (bird) could be a useful design device instead of the commonly seen illustrated mountain landscape (which is quite common for our local wines). Label size 90 high, 110 wide. Please use a pinot noir / burgundy bottle. See here for vineyard pics, and also below pics for other local wine labels and pics for inspiration / styles. https://www.instagram.com/jan.ter.bosch/

Target Market(s)

average bottle price for this premium red pinot noir would be aroundUS$40. target market are generally urban professionals aged 25 and older with a high degree of interest in pinot noir wine, and who are familiar with New Zealand pinot noir (ie. already know several brands).

Colors
ed252d

Requirements
Must have
• distinctive label, sophisticated look
Nice to have
• classy white paper stock
Should not have
• label must not get too busy... less but high quality and distinctive is more....

```html
<!DOCTYPE html>
<html lang="en">
<head>
<meta charset="utf-8">
<title>Wren – ter Bosch vineyard – Pinot Noir label</title>
<link rel="stylesheet" href="https://fonts.googleapis.com/css2?family=Crimson+Text:wght@400&family=Josefin+Sans:wght@300&display=swap">
<style>
  :root {
    --backdrop: #b11f27;
    --paper: #f6f4f4;
    --paper-shade: #ece6e7;
    --wine: #a1121d;
    --ink: #2a2a2a;
    --rule: #8e1019;
  }
  html, body {
    margin: 0;
    padding: 0;
    width: 1200px;
    height: 800px;
    overflow: hidden;
    background: var(--backdrop);
  }
  .canvas {
    position: relative;
    width: 1200px;
    height: 800px;
  }
  .label {
    position: absolute;
    left: 250px;
    top: 113px;
    width: 700px;
    height: 574px;
    background: var(--paper);
    overflow: hidden;
    box-shadow: 0 18px 40px rgba(60, 0, 5, 0.35);
  }
  .label__pattern {
    position: absolute;
    inset: 0;
    background: linear-gradient(160deg, var(--paper) 0%, var(--paper-shade) 100%);
  }
  .label__rules {
    position: absolute;
    inset: 0;
  }
  .label__column {
    position: absolute;
    top: 0;
    height: 574px;
    margin: 0;
    display: flex;
    align-items: center;
    justify-content: center;
    writing-mode: vertical-rl;
    white-space: nowrap;
    line-height: 1;
  }
  .label__region {
    left: 112px;
    width: 40px;
    font-family: "Josefin Sans", sans-serif;
    font-weight: 300;
    font-size: 22px;
    letter-spacing: 0.25em;
    color: var(--ink);
  }
  .label__vineyard {
    left: 192px;
    width: 50px;
    font-family: "Crimson Text", serif;
    font-size: 40px;
    color: var(--wine);
  }
  .label__brand {
    left: 330px;
    width: 220px;
    font-family: "Crimson Text", serif;
    font-weight: 400;
    font-size: 150px;
    letter-spacing: 0.06em;
    color: var(--wine);
  }
</style>
</head>
<body>
  <main class="canvas">
    <section class="label" aria-label="Wren Pinot Noir wine label">
      <div class="label__pattern" role="img" aria-label="Faint line pattern of small birds in soft red on white paper"></div>

      <svg class="label__rules" width="700" height="574" viewBox="0 0 700 574" aria-hidden="true">
        <g stroke="var(--rule)" stroke-width="4" fill="none" stroke-linecap="round">
          <line x1="90" y1="0" x2="90" y2="574"/>
          <line x1="22" y1="175" x2="90" y2="120"/>
          <line x1="22" y1="205" x2="90" y2="150"/>
          <line x1="650" y1="0" x2="650" y2="574"/>
          <line x1="650" y1="380" x2="700" y2="340"/>
          <line x1="650" y1="410" x2="700" y2="370"/>
        </g>
      </svg>

      <p class="label__column label__region">RAVENSDALE, HIGH COUNTRY</p>
      <p class="label__column label__vineyard">ter Bosch vineyard</p>
      <h1 class="label__column label__brand">WREN</h1>
    </section>
  </main>
</body>
</html>
```